Design business cards for Ironvale Barbers (Opening March so won't need finalised till January2018

Ironvale Barbers is the new age barbers and skincare for all men. Creating tailor made haircuts & customised skincare solutions for the perfect healthy manly look. The Barbers will have a industrial, rustic, worldly feel about it. Rustic red brick wall with old wine barrels as the work stations with the old fashion barber chairs. Concrete floor and a bit corrugated iron around.
Target Market(s)
Professional males who like a great haircut, wet shave and may consider a facial if in the right environment. Total pampering experience in a boys environment.
Industry/Entity Type
Barber
Contact Information for Business Card
Front- Logo - address is 42 Kowhai Rd Taupo
Ph - (07) 548 9163
www.ironvalebarbers.com
email - hello@ironvale.co.nz
Back of card
Mens Haircare - Wet Shaving - Facials - Skin Prescriptions
We are doing a loyalty program - 6 squares numbered then 7th free
Colors
Designer to choose colors to be used in the design.
Requirements
Must have
- Clean simple easy to read.
Nice to have
- Our current colours are white font on black background but thinking we need to introduce another colour. Maybe white logo on a copper, bronze or rusty background. Or even a rustic red brick wall with white writing. Want it clean simple to read. Maybe a burgundy?
Should not have
- no images like heads, scissors, razors please

```html
<!DOCTYPE html>
<html lang="en">
<head>
<meta charset="utf-8">
<title>Ironvale Barbers — Business Card</title>
<link rel="stylesheet" href="https://fonts.googleapis.com/css2?family=Alegreya:wght@700&display=swap">
<style>
  :root {
    --page: #ffffff;
    --brick-light: #b85a33;
    --brick-mid: #a54a2b;
    --brick-dark: #8e3d25;
    --chalk: #f2eee6;
  }
  html, body {
    margin: 0;
    width: 1200px;
    height: 1000px;
    overflow: hidden;
    background: var(--page);
  }
  .canvas {
    position: relative;
    width: 1200px;
    height: 1000px;
    font-family: "Alegreya", Georgia, serif;
    font-weight: 700;
    color: var(--chalk);
  }
  .card {
    position: absolute;
    width: 552px;
    height: 372px;
    border-radius: 22px;
    overflow: hidden;
  }
  .card--front { left: 52px; top: 58px; }
  .card--back { left: 605px; top: 546px; }
  .brick-wall {
    position: absolute;
    inset: 0;
    background: linear-gradient(160deg, var(--brick-light) 0%, var(--brick-mid) 55%, var(--brick-dark) 100%);
  }
  .brand {
    position: absolute;
    left: 0;
    right: 0;
    text-align: center;
    line-height: 1;
  }
  .brand__name {
    display: block;
    font-size: 70px;
    letter-spacing: 1px;
    text-transform: uppercase;
  }
  .brand__trade {
    display: block;
    margin-top: 8px;
    font-size: 26px;
    letter-spacing: 8px;
    text-transform: uppercase;
  }
  .card--front .brand { top: 62px; }
  .card--back .brand { top: 66px; }
  .contact {
    position: absolute;
    top: 208px;
    left: 0;
    right: 0;
    margin: 0;
    padding: 0;
    list-style: none;
    text-align: center;
    font-size: 15px;
    line-height: 26.5px;
  }
  .rules {
    position: absolute;
    inset: 0;
  }
  .services {
    position: absolute;
    top: 216px;
    left: 0;
    right: 0;
    text-align: center;
    font-size: 20px;
    letter-spacing: 2px;
    line-height: 28px;
  }
  .appointment {
    position: absolute;
    top: 343px;
    font-size: 15px;
  }
  .appointment--date { left: 46px; }
  .appointment--time { left: 328px; }
</style>
</head>
<body>
<main class="canvas">

  <section class="card card--front" aria-label="Card front">
    <div class="brick-wall" role="img" aria-label="Weathered red brick wall texture"></div>
    <div class="brand">
      <span class="brand__name">Ironvale</span>
      <span class="brand__trade">Barbers</span>
    </div>
    <svg class="rules" width="552" height="372" viewBox="0 0 552 372" aria-hidden="true">
      <g stroke="#f2eee6" stroke-width="2">
        <line x1="122" y1="212" x2="180" y2="212"/>
        <line x1="432" y1="212" x2="500" y2="212"/>
        <line x1="0" y1="272" x2="125" y2="272"/>
        <line x1="425" y1="272" x2="552" y2="272"/>
        <line x1="60" y1="300" x2="165" y2="300"/>
        <line x1="410" y1="300" x2="530" y2="300"/>
      </g>
    </svg>
    <ul class="contact">
      <li>42 Kowhai Rd.Taupo</li>
      <li>Phone</li>
      <li>www.ironvalebarbers.com</li>
      <li>hello@ironvale.co.nz</li>
    </ul>
  </section>

  <section class="card card--back" aria-label="Card back">
    <div class="brick-wall" role="img" aria-label="Weathered red brick wall texture"></div>
    <div class="brand">
      <span class="brand__name">Ironvale</span>
      <span class="brand__trade">Barbers</span>
    </div>
    <p class="services" style="margin:0">
      Mens Haircare &nbsp;- &nbsp;Wet Shaving<br>
      Facials &nbsp;- &nbsp;Skin Prescriptions
    </p>
    <span class="appointment appointment--date">Date:</span>
    <span class="appointment appointment--time">Time:</span>
  </section>

</main>
</body>
</html>
```